Spin Dash 4 Fun business card

Spin Dash 4 Fun is a national UK campaign that promotes the value of play for children. The website has recently undergone a redesign and will soon be going live, this business card design will need to reflect the new website's design and colour scheme, etc.
Key wording/info for inclusion (front)
- Strapline titles
A little Play every day (in caps)
giving you great free play ideas, everyday!
- Logo
Key wording for inclusion (rear)
- Download our free play app - Spin Dash 4 Fun
- Visit our website - www.spindash4fun.co.uk
- To share hints and tips with other parents
www.facebook.com/spindashforfun
- Want to get involved in the campaign? No matter who you are we would love to hear from you! Email - getinvolved@spindashforfun.co.uk
Social media icons
Facebook facebook.com/spindash4fun
Twitter @spindash4fun
Youtube youtube.com/spindashforfun
The target audience is parents of young children up to the age of 12.
Please note that all attached graphics are the property of the Northern Craft & Pastime Guild and must only be used for the purpose of this project.
Updates
Please note the design we are seeking will be in a business card 'shape' but will not be for a specific 'person' or name as such. We are looking for a colourful and modern design which is not 'corporate. Thank you.
Target Market(s)
Industry/Entity Type
Business
Look and feel
Each slider illustrates characteristics of the customer's brand and the style your logo design should communicate.

```html
<!DOCTYPE html>
<html lang="en">
<head>
<meta charset="utf-8">
<title>Spin Dash 4 Fun – Business Card</title>
<link href="https://fonts.googleapis.com/css2?family=Nunito:wght@600;700;800;900&display=swap" rel="stylesheet">
<style>
  :root {
    --page: #2a2a2c;
    --green: #a9cf38;
    --blue: #1fb1e6;
    --sky: #bfe5f7;
    --pink: #ee5b8a;
    --yellow: #fde02f;
    --purple: #6a3fa0;
    --ink: #555a60;
    --link: #1b9fd8;
    --white: #ffffff;
  }
  * { box-sizing: border-box; margin: 0; padding: 0; }
  html, body { width: 1200px; height: 1000px; overflow: hidden; }
  body {
    background: var(--page);
    font-family: "Nunito", "Arial Rounded MT Bold", sans-serif;
    position: relative;
  }
  .card {
    position: absolute;
    left: 240px;
    width: 720px;
    height: 440px;
    border-radius: 24px;
    overflow: hidden;
    box-shadow: 0 14px 30px rgba(0,0,0,.45);
  }
  .card svg.card-art { position: absolute; inset: 0; }
  .card-front { top: 40px; }
  .card-back { top: 520px; }

  /* front */
  .strapline {
    position: absolute; left: 60px; top: 148px; width: 390px;
    color: var(--white); font-weight: 900; font-size: 27px; text-align: center; white-space: nowrap;
  }
  .promise {
    position: absolute; left: 270px; top: 292px; width: 380px;
    color: var(--white); font-weight: 900; font-size: 30px; line-height: 1.12; text-align: center; white-space: nowrap;
  }
  .brand-name {
    color: var(--purple); font-weight: 900; text-align: center; line-height: 1.05; white-space: nowrap;
  }
  .card-front .brand-name {
    position: absolute; left: 500px; top: 133px; width: 200px; font-size: 32px;
  }

  /* back */
  .card-back .brand-name {
    position: absolute; left: 40px; top: 42px; width: 200px; font-size: 32px;
  }
  .prompt {
    position: absolute; color: var(--ink); font-weight: 800; font-size: 15px; line-height: 1.1; text-align: right;
  }
  .prompt-app { left: 246px; top: 74px; width: 160px; }
  .prompt-app em { color: var(--link); font-style: normal; }
  .prompt-share { left: 256px; top: 170px; width: 150px; }
  .channel {
    position: absolute; left: 462px; color: var(--white); font-weight: 800; font-size: 23px; white-space: nowrap;
  }
  .involve {
    position: absolute; left: 34px; top: 266px; width: 392px; color: var(--ink);
  }
  .involve h2 { font-size: 18px; font-weight: 900; white-space: nowrap; }
  .involve p { font-size: 17px; font-weight: 700; line-height: 1.15; margin-top: 2px; }
  .email {
    position: absolute; left: 34px; top: 342px; display: flex; align-items: center; gap: 8px;
    color: var(--link); font-weight: 800; font-size: 17px; white-space: nowrap;
  }
</style>
</head>
<body>

<section class="card card-front" aria-label="Card front">
  <svg class="card-art" width="720" height="440" viewBox="0 0 720 440">
    <defs>
      <linearGradient id="photoTone" x1="0" y1="0" x2="1" y2="1">
        <stop offset="0" stop-color="#c8332f"/>
        <stop offset=".35" stop-color="#e8b59a"/>
        <stop offset=".7" stop-color="#8fc146"/>
        <stop offset="1" stop-color="#5c8f2e"/>
      </linearGradient>
    </defs>
    <rect width="720" height="440" fill="url(#photoTone)" role="img" aria-label="Photo of smiling children lying on grass making goggles with their hands"/>
    <circle cx="640" cy="470" r="190" fill="var(--pink)"/>
    <circle cx="470" cy="510" r="312" fill="var(--yellow)"/>
    <circle cx="460" cy="520" r="300" fill="var(--blue)"/>
    <ellipse cx="255" cy="165" rx="250" ry="76" fill="var(--green)"/>
    <circle cx="600" cy="160" r="112" fill="var(--white)"/>
  </svg>
  <p class="strapline">A little play every day</p>
  <p class="promise">Giving you<br>great free play ideas,<br>every day!</p>
  <p class="brand-name">Spin Dash<br>4 Fun</p>
</section>

<section class="card card-back" aria-label="Card back">
  <svg class="card-art" width="720" height="440" viewBox="0 0 720 440">
    <defs>
      <linearGradient id="skyFade" x1="0" y1="0" x2="0" y2="1">
        <stop offset="0" stop-color="var(--sky)"/>
        <stop offset=".6" stop-color="#e3f4fc"/>
        <stop offset=".85" stop-color="#ffffff"/>
      </linearGradient>
    </defs>
    <rect width="720" height="440" fill="url(#skyFade)"/>
    <ellipse cx="140" cy="78" rx="130" ry="52" fill="var(--white)" opacity=".9"/>
    <path d="M0 378 C 120 372, 220 400, 330 404 S 420 412, 430 414" fill="none" stroke="var(--green)" stroke-width="2" opacity=".6"/>
    <rect x="430" y="100" width="290" height="92" fill="var(--pink)"/>
    <rect x="430" y="192" width="290" height="86" fill="var(--blue)"/>
    <rect x="430" y="278" width="290" height="84" fill="var(--green)"/>
    <rect x="430" y="362" width="290" height="78" fill="var(--yellow)"/>
    <g fill="var(--link)">
      <path d="M412 110 l14 6 -14 6z"/>
      <path d="M412 198 l14 6 -14 6z"/>
    </g>
    <g stroke="var(--white)" stroke-width="3" fill="#8a8f96">
      <circle cx="440" cy="146" r="14"/>
      <circle cx="440" cy="235" r="14"/>
      <circle cx="440" cy="320" r="14"/>
      <circle cx="440" cy="401" r="14"/>
    </g>
  </svg>
  <p class="brand-name">Spin Dash<br>4 Fun</p>
  <p class="prompt prompt-app">Download our<br><em>free play app @</em></p>
  <p class="prompt prompt-share">To share hints<br>and tips with<br>other parents</p>
  <p class="channel" style="top:132px">spindash4fun.co.uk</p>
  <p class="channel" style="top:221px">spindash4fun</p>
  <p class="channel" style="top:306px">spindash4fun</p>
  <p class="channel" style="top:387px">spindashforfun</p>
  <div class="involve">
    <h2>Want to get involved in the campaign?</h2>
    <p>No matter who you are we would love<br>to hear from you!</p>
  </div>
  <p class="email">
    <svg width="18" height="14" viewBox="0 0 18 14" aria-hidden="true"><rect x="1" y="1" width="16" height="12" fill="none" stroke="var(--ink)" stroke-width="1.6"/><path d="M1 1 L9 8 L17 1" fill="none" stroke="var(--ink)" stroke-width="1.6"/></svg>
    getinvolved@spindash4fun.co.uk
  </p>
</section>

</body>
</html>
```